Calvoterra business card

a nice business card with the logo,
Calvoterra
Teresa Lindqvist
Marketing Director
CH-1563 Geneva
Switzerland
+41 76 382 1904
email: Teresa.Lindqvist@calvoterra-mail.example

Target Market(s)

fertilizer business people, very nice and classic business card, normal size, make it nice and funky, try to make it different from the normal boring ones if possible.

Industry/Entity Type

Farming

Number of Pages Required

1 page

Requirements
Must have
• logo, Calvoterra, my name - mail and phone number
regular business card size for me to print easy please

```html
<!DOCTYPE html>
<html lang="en">
<head>
<meta charset="utf-8">
<title>Calvoterra business cards</title>
<link rel="stylesheet" href="https://fonts.googleapis.com/css2?family=Arimo:wght@400;700&display=swap">
<style>
  :root {
    --leaf-green: #acd52b;
    --pale-straw: #ebe9a7;
    --paper: #ffffff;
    --ink: #111111;
    --edge: #6a6a6a;
  }
  * { margin: 0; padding: 0; box-sizing: border-box; }
  html, body {
    width: 736px;
    height: 1200px;
    overflow: hidden;
    background: var(--paper);
    font-family: "Arimo", Arial, sans-serif;
    color: var(--ink);
  }
  .sheet { position: relative; width: 736px; height: 1200px; }

  .card {
    position: absolute;
    width: 341px;
    height: 582px;
    border: 1px solid var(--edge);
    overflow: hidden;
  }
  .card--straw { background: var(--pale-straw); }
  .card--white { background: var(--paper); }
  .card--a { left: 5px;   top: 0; }
  .card--b { left: 394px; top: 0; }
  .card--c { left: 0;     top: 617px; }
  .card--d { left: 394px; top: 617px; }

  .brand-band {
    position: absolute;
    left: 0; right: 0;
    height: 71px;
    background: var(--leaf-green);
    color: var(--paper);
    font-weight: 700;
    font-size: 36px;
    line-height: 71px;
    text-align: center;
    letter-spacing: 0.5px;
  }
  .brand-band--top { top: 0; }
  .brand-band--bottom { bottom: 0; }

  .line {
    position: absolute;
    left: 0; right: 0;
    text-align: center;
    transform: translateY(-50%);
    white-space: nowrap;
  }
  .person-name { font-size: 21px; }
  .person-role { font-size: 16px; }
  .contact { font-size: 16.5px; }
  .contact--email { font-size: 13.5px; }

  .brand-mark {
    position: absolute;
    left: 50%;
    width: 64px;
    height: 64px;
    margin-left: -32px;
    border-radius: 50%;
    background: var(--leaf-green);
  }
  .brand-wordmark {
    font-size: 13px;
    font-weight: 700;
    letter-spacing: 4px;
  }
</style>
</head>
<body>
<main class="sheet">

  <!-- Straw card, band on top -->
  <section class="card card--straw card--a">
    <div class="brand-band brand-band--top">CALVOTERRA</div>
    <p class="line person-name" style="top:116px">Teresa Lindqvist</p>
    <p class="line person-role" style="top:142px">Marketing Director</p>
    <div class="brand-mark" style="top:235px"></div>
    <p class="line brand-wordmark" style="top:362px">CALVOTERRA</p>
    <p class="line contact" style="top:459px">CH-1563 Geneva Switzerland</p>
    <p class="line contact" style="top:479px">+41 76 382 1904</p>
    <p class="line contact" style="top:508px">Email:</p>
    <p class="line contact contact--email" style="top:528px">Teresa.Lindqvist@calvoterra-mail.example</p>
  </section>

  <!-- White card, band on top -->
  <section class="card card--white card--b">
    <div class="brand-band brand-band--top">CALVOTERRA</div>
    <p class="line person-name" style="top:116px">Teresa Lindqvist</p>
    <p class="line person-role" style="top:142px">Marketing Director</p>
    <div class="brand-mark" style="top:235px"></div>
    <p class="line brand-wordmark" style="top:362px">CALVOTERRA</p>
    <p class="line contact" style="top:459px">CH-1563 Geneva Switzerland</p>
    <p class="line contact" style="top:479px">+41 76 382 1904</p>
    <p class="line contact" style="top:508px">Email:</p>
    <p class="line contact contact--email" style="top:528px">Teresa.Lindqvist@calvoterra-mail.example</p>
  </section>

  <!-- White card, band at bottom -->
  <section class="card card--white card--c">
    <div class="brand-mark" style="top:60px"></div>
    <p class="line brand-wordmark" style="top:187px">CALVOTERRA</p>
    <p class="line person-name" style="top:243px">Teresa Lindqvist</p>
    <p class="line person-role" style="top:269px">Marketing Director</p>
    <p class="line contact" style="top:353px">CH-1563 Geneva Switzerland</p>
    <p class="line contact" style="top:373px">+41 76 382 1904</p>
    <p class="line contact" style="top:469px">Email:</p>
    <p class="line contact contact--email" style="top:489px">Teresa.Lindqvist@calvoterra-mail.example</p>
    <div class="brand-band brand-band--bottom">CALVOTERRA</div>
  </section>

  <!-- Straw card, band at bottom -->
  <section class="card card--straw card--d">
    <div class="brand-mark" style="top:60px"></div>
    <p class="line brand-wordmark" style="top:187px">CALVOTERRA</p>
    <p class="line person-name" style="top:243px">Teresa Lindqvist</p>
    <p class="line person-role" style="top:269px">Marketing Director</p>
    <p class="line contact" style="top:353px">CH-1563 Geneva Switzerland</p>
    <p class="line contact" style="top:373px">+41 76 382 1904</p>
    <p class="line contact" style="top:469px">Email:</p>
    <p class="line contact contact--email" style="top:489px">Teresa.Lindqvist@calvoterra-mail.example</p>
    <div class="brand-band brand-band--bottom">CALVOTERRA</div>
  </section>

</main>
</body>
</html>
```